Velvet Lune Fashion Boutigue Website

The Velvet Lune Fashion Boutique is located in Toronto, Canada. We carry high quality, elegant line of clothing including dresses and gowns for women.
Our goal is to help ladies find elegant outfits for any occasions.

I've created the domain - (WorldPress) - http://velvetlune.style/
I need you to:
Design and build my website
Features I need: Home, Visit us (location),About us, Contact us, Book an appointment, Appointment confirmation, Gallery/Products, Events, Links to our social media channels, Sign up for promotions, Collaboration Opportunities for Models, Videos, Size Finder.

I will provide you with images of our collection and a short video, but for the homepage I would like you to utilize elegant, eye-catching and breathtaking images for different pages.

```html
<!DOCTYPE html>
<html lang="en">
<head>
<meta charset="utf-8">
<title>Velvet Lune Fashion Boutique</title>
<link href="https://fonts.googleapis.com/css2?family=Nunito+Sans:wght@300;400;600;700&display=swap" rel="stylesheet">
<style>
:root{
  --gold:#c49a5e;
  --gold-line:#d2a867;
  --ink:#2b2b2b;
  --muted:#6e6e6e;
  --dark:#1e1e1e;
  --light:#f3f2f5;
  --grey:#efefef;
  --white:#ffffff;
}
*{margin:0;padding:0;box-sizing:border-box}
html,body{width:1200px;height:3130px;overflow:hidden}
body{font-family:"Nunito Sans",Arial,sans-serif;color:var(--ink);background:var(--white);position:relative}
.section{position:absolute;left:0;width:1200px;overflow:hidden}
.abs{position:absolute}
.fill{position:absolute}

/* hero */
.hero{top:0;height:512px;border-bottom:6px solid var(--gold-line)}
.hero-bg{inset:0;background:linear-gradient(100deg,#cfe9e6 0%,#eef2ef 40%,#f5eee2 75%,#f3e6cf 100%)}
.hero-model{left:470px;top:60px;width:700px;height:446px;background:radial-gradient(ellipse at 55% 55%,#dccab3 0%,#ead9c2 45%,rgba(243,230,210,0) 75%)}
.brand-box{left:86px;top:0;width:238px;height:130px;background:#1b1b1b;display:flex;flex-direction:column;align-items:center;justify-content:flex-end;padding-bottom:16px}
.brand-mark{width:22px;height:22px;border-radius:50%;background:var(--gold);margin-bottom:14px}
.brand-name{color:var(--white);font-size:24px;font-weight:400;letter-spacing:2px}
.brand-tag{color:var(--gold);font-size:10px;letter-spacing:2px;margin-top:3px}
.hero-panel{left:86px;top:130px;width:238px;height:298px;background:rgba(255,255,255,.88)}
.hero-panel p{position:absolute;top:40px;left:52px;right:52px;text-align:center;font-size:21px;line-height:26px;font-weight:400;color:#333}
.btn{display:flex;align-items:center;justify-content:center;border:2px solid #bdbdbd;background:var(--white);color:var(--gold);font-size:12px;letter-spacing:1px;text-transform:uppercase}
.hero .btn{left:86px;top:388px;width:238px;height:36px}
.nav{top:31px;left:518px;display:flex;gap:20px;font-size:14px;color:#333;align-items:center}
.nav .active{border-bottom:2px solid var(--gold);padding-bottom:2px}
.nav .sep{width:1px;height:16px;background:var(--gold)}
.nav .phone{display:flex;align-items:center;gap:6px}
.dots{display:flex;gap:5px}
.dots i{width:9px;height:9px;border-radius:50%;background:#d8d8d8;display:block}
.dots i.on{background:var(--white)}
.hero .dots{left:576px;top:488px}

/* about */
.about{top:518px;height:323px;background:var(--light)}
.about-photo{left:167px;top:0;width:334px;height:323px;background:linear-gradient(160deg,#9a9a9e 0%,#4b4b52 55%,#1d1d22 100%)}
.about h2{left:586px;top:62px;font-size:32px;line-height:42px;font-weight:400;color:#222;letter-spacing:1px}
.about p{left:588px;top:152px;width:390px;font-size:13px;line-height:22px;color:var(--muted)}
.link{font-size:12px;text-decoration:underline;text-transform:uppercase;letter-spacing:.5px}
.about .link{left:588px;top:210px;color:#333}

/* products */
.products{top:841px;height:347px;background:var(--dark)}
.products h2{left:86px;top:78px;font-size:32px;font-weight:400;color:var(--gold);letter-spacing:1px}
.products p{left:86px;top:126px;width:250px;font-size:13px;line-height:21px;color:#9a9a9a}
.products .arrows{left:86px;top:242px}
.tiles{left:405px;top:61px;width:710px;height:225px;display:flex}
.tile{flex:1;position:relative}
.tile-1{background:linear-gradient(180deg,#eee6e2,#cdb7a8)}
.tile-2{background:#8f8f8f}
.tile-3{background:linear-gradient(180deg,#d8cbbf,#a99583)}
.tile-caption{position:absolute;top:84px;left:0;right:0;text-align:center;color:var(--white)}
.tile-caption strong{display:block;font-size:14px;font-weight:400;letter-spacing:.5px}
.tile-caption span{display:block;margin-top:10px;font-size:12px;text-decoration:underline}

/* events */
.events{top:1188px;height:592px;background:var(--white)}
.section-title{width:100%;text-align:center;font-size:32px;font-weight:400;letter-spacing:1px;color:#222}
.events .section-title{top:54px}
.ev-main{left:86px;top:112px;width:511px;height:194px;background:linear-gradient(90deg,#3a3636,#6d5a55 50%,#4a4245)}
.ev-main .shade{inset:0;background:rgba(0,0,0,.35)}
.ev-text{left:26px;top:38px;color:var(--white);font-size:13px;line-height:24px}
.ev-text h3{font-size:15px;font-weight:400;margin-bottom:2px;letter-spacing:.5px}
.ev-text .link{display:block;margin-top:12px;color:#ddd}
.ev-date{left:402px;top:36px;width:70px;height:24px;background:var(--white);color:var(--gold);font-size:11px;display:flex;align-items:center;justify-content:center}
.ev-a{left:86px;top:310px;width:256px;height:220px;background:linear-gradient(160deg,#6a5240,#c69a2c 55%,#7a3a24)}
.ev-b{left:345px;top:310px;width:252px;height:220px;background:linear-gradient(160deg,#c8262a,#3b6ea0 60%,#c2262c)}
.ev-c{left:601px;top:112px;width:514px;height:418px;background:linear-gradient(150deg,#e9e9ea,#cfd0d2 50%,#8aa2b8 100%)}

/* testimonial */
.quote{top:1780px;height:318px;background:linear-gradient(180deg,#151515 0%,#2a2a2a 55%,#3a1414 100%)}
.quote-mark{left:580px;top:62px}
.quote p{left:82px;top:108px;width:1036px;text-align:center;color:#e6e6e6;font-size:12px;line-height:21px}
.quote cite{left:0;top:206px;width:100%;text-align:center;color:var(--white);font-size:13px;font-style:normal;font-weight:600}
.quote .dots{left:581px;top:244px}
.quote .dots i{background:var(--white)}
.quote .dots i.on{background:var(--gold)}

/* collaboration */
.collab{top:2098px;height:500px;background:var(--white)}
.collab-card{left:86px;top:62px;width:1029px;height:376px;box-shadow:0 4px 16px rgba(0,0,0,.25)}
.collab-panel{left:0;top:0;width:348px;height:376px;background:var(--gold)}
.collab-panel h2{left:44px;top:64px;font-size:30px;line-height:42px;font-weight:400;color:var(--white);letter-spacing:.5px}
.collab-panel p{left:44px;top:192px;width:250px;font-size:12px;line-height:19px;color:#f6ead8}
.collab-panel .btn{left:44px;top:268px;width:236px;height:34px;border-color:#e3e3e3}
.collab-video{left:348px;top:0;width:681px;height:376px;background:radial-gradient(ellipse at 75% 40%,#8a5a2a 0%,#4a2a14 45%,#1c1008 100%)}
.play{left:288px;top:126px}
.collab-video .link{left:0;top:260px;width:100%;text-align:center;color:var(--white)}

/* newsletter */
.newsletter{top:2598px;height:278px;background:var(--grey)}
.newsletter .section-title{top:54px;font-size:30px}
.newsletter p{left:0;top:103px;width:100%;text-align:center;font-size:13px;color:#555}
.field{left:357px;top:130px;width:492px;height:32px;background:var(--white);font-size:12px;color:#666;padding:8px 10px}
.newsletter .btn{left:482px;top:182px;width:236px;height:34px}

/* footer */
.footer{top:2876px;height:254px;background:var(--gold);color:var(--white)}
.footer h4{font-size:15px;font-weight:400;letter-spacing:.5px;margin-bottom:14px;color:#fff}
.footer .col{top:58px;font-size:12.5px;line-height:21px}
.col-size{left:86px;width:250px}
.col-size .btn{width:236px;height:34px;margin-top:18px;border-color:#e8e8e8}
.col-contact{left:403px;width:220px}
.col-contact b{font-weight:700}
.col-contact .row{display:flex;align-items:center;gap:8px}
.col-products{left:655px}
.col-social{left:803px}
.col-social .row{display:flex;align-items:center;gap:9px}
.col-social .row i{width:8px;height:8px;border-radius:50%;background:var(--white);display:block}
.footer-brand{left:958px;top:58px;width:157px;height:84px;background:#1b1b1b;display:flex;flex-direction:column;align-items:center;justify-content:center;gap:5px}
.footer-brand .brand-mark{width:12px;height:12px;margin:0}
.footer-brand .brand-name{font-size:16px;letter-spacing:1.5px}
.copy{left:958px;top:154px;font-size:12px;line-height:19px}
</style>
</head>
<body>

<header class="section hero">
  <div class="fill hero-bg" role="img" aria-label="Soft pastel studio backdrop"></div>
  <div class="fill hero-model" role="img" aria-label="Model in a beaded champagne evening gown reclining on the studio floor"></div>
  <div class="abs brand-box">
    <span class="brand-mark"></span>
    <span class="brand-name">VELVET LUNE</span>
    <span class="brand-tag">FASHION BOUTIQUE</span>
  </div>
  <div class="abs hero-panel"><p>High Quality, Elegant Line of Clothing including Dresses and Gowns for Women</p></div>
  <a class="abs btn">Make an Appointment</a>
  <nav class="abs nav">
    <span class="active">HOME</span><span>VISIT US</span><span>ABOUT US</span><span>PRODUCTS</span><span>EVENTS</span><span>CONTACT US</span>
    <span class="sep"></span>
    <span class="phone"><svg width="12" height="12" viewBox="0 0 24 24"><path fill="#c49a5e" d="M6.6 10.8a15 15 0 0 0 6.6 6.6l2.2-2.2a1 1 0 0 1 1-.25 11.4 11.4 0 0 0 3.6.6 1 1 0 0 1 1 1V20a1 1 0 0 1-1 1A17 17 0 0 1 3 4a1 1 0 0 1 1-1h3.5a1 1 0 0 1 1 1c0 1.25.2 2.45.6 3.6a1 1 0 0 1-.25 1z"/></svg>416 555 0142</span>
  </nav>
  <div class="abs dots"><i class="on"></i><i></i><i></i></div>
</header>

<section class="section about">
  <div class="fill about-photo" role="img" aria-label="Woman in a black hat holding a shopping bag"></div>
  <h2 class="abs">ELEGANT OUTFITS<br>FOR ANY OCCASIONS</h2>
  <p class="abs">It is a long established fact that a reader will be distracted by the readable content of a page when looking at its layout.</p>
  <a class="abs link">Read more about us</a>
</section>

<section class="section products">
  <h2 class="abs">OUR PRODUCTS</h2>
  <p class="abs">There are many variations of passages of Lorem Ipsum available, but the majority have suffered alteration.</p>
  <svg class="abs arrows" width="56" height="14" viewBox="0 0 56 14">
    <path d="M2 7h20M2 7l5-5M2 7l5 5" stroke="#c49a5e" stroke-width="2" fill="none"/>
    <path d="M32 7h20M52 7l-5-5M52 7l-5 5" stroke="#ffffff" stroke-width="2" fill="none"/>
  </svg>
  <div class="abs tiles">
    <div class="tile tile-1" role="img" aria-label="Model in a flowing blush gown"></div>
    <div class="tile tile-2" role="img" aria-label="Model in a black cocktail dress">
      <div class="tile-caption"><strong>CONTRAY TO POPULAR</strong><span>VIEW DETAILS</span></div>
    </div>
    <div class="tile tile-3" role="img" aria-label="Model in a sequined silver gown"></div>
  </div>
</section>

<section class="section events">
  <h2 class="abs section-title">EVENTS</h2>
  <div class="abs ev-main" role="img" aria-label="Rack of dresses at a boutique event">
    <div class="fill shade"></div>
    <div class="abs ev-text">
      <h3>CONTRAY TO POPULAR</h3>
      All the Lorem Ipsum generators on the Internet.<br>
      LOCATION: Lorem Ipsum
      <span class="link">View details</span>
    </div>
    <div class="abs ev-date">24th MAY</div>
  </div>
  <div class="abs ev-a" role="img" aria-label="Woman in a mustard sweater seated on wooden steps"></div>
  <div class="abs ev-b" role="img" aria-label="Woman in a plaid coat against a red wall"></div>
  <div class="abs ev-c" role="img" aria-label="Two friends in beanies posing against a white brick wall"></div>
</section>

<section class="section quote" role="img" aria-label="Dim runway hall with a red carpet">
  <svg class="abs quote-mark" width="40" height="32" viewBox="0 0 40 32"><path fill="#fff" d="M0 32V18C0 8 5 2 15 0l2 4c-5 2-7 5-7 10h7v18zm22 0V18c0-10 5-16 15-18l2 4c-5 2-7 5-7 10h7v18z"/></svg>
  <p class="abs">It is a long established fact that a reader will be distracted by the readable content of a page when looking at its layout. The point of using Lorem Ipsum is that it has a more-or-less normal distribution of letters, as opposed to using 'Content here, content here', making it look like readable English. Many desktop publishing packages and web page editors now use Lorem Ipsum as their default model text, and a search for 'lorem ipsum' will uncover many web sites still in their infancy. Various versions have evolved over the years, sometimes by accident, sometimes on purpose (injected humour and the like).</p>
  <cite class="abs">CLARA HAYES (Businesswoman)</cite>
  <div class="abs dots"><i class="on"></i><i></i><i></i></div>
</section>

<section class="section collab">
  <div class="abs collab-card">
    <div class="abs collab-panel">
      <h2 class="abs">COLLABORATION<br>OPPORTUNITIES<br>FOR MODELS</h2>
      <p class="abs">There are many variations of passages of Lorem Ipsum available, but the majority have suffered alteration.</p>
      <a class="abs btn">Click here</a>
    </div>
    <div class="abs collab-video" role="img" aria-label="Video still of a model in a wide-brim hat in a warm-lit lounge">
      <svg class="abs play" width="86" height="86" viewBox="0 0 86 86"><circle cx="43" cy="43" r="40" fill="none" stroke="#fff" stroke-width="2"/><path d="M35 27v32l25-16z" fill="none" stroke="#fff" stroke-width="2"/></svg>
      <span class="abs link">Watch more videos</span>
    </div>
  </div>
</section>

<section class="section newsletter">
  <h2 class="abs section-title">SUBSCRIBE OUR NEWSLETTER</h2>
  <p class="abs">It is a long established fact that a reader will be distracted</p>
  <div class="abs field">Email</div>
  <a class="abs btn">Sign up now</a>
</section>

<footer class="section footer">
  <div class="abs col col-size">
    <h4>GET YOUR SIZE</h4>
    Lorem Ipsum is simply dummy text of the printing and typesetting industry.
    <a class="btn">Size finder</a>
  </div>
  <div class="abs col col-contact">
    <h4>CONTACT INFO</h4>
    <b>ADDRESS</b><br>48 Linden Row, Toronto,<br>Canada M5V 2K1
    <div class="row"><svg width="10" height="10" viewBox="0 0 24 24"><path fill="#fff" d="M6.6 10.8a15 15 0 0 0 6.6 6.6l2.2-2.2a1 1 0 0 1 1-.25 11.4 11.4 0 0 0 3.6.6 1 1 0 0 1 1 1V20a1 1 0 0 1-1 1A17 17 0 0 1 3 4a1 1 0 0 1 1-1h3.5a1 1 0 0 1 1 1c0 1.25.2 2.45.6 3.6a1 1 0 0 1-.25 1z"/></svg>416 555 0187</div>
    <div class="row"><svg width="11" height="9" viewBox="0 0 22 16"><rect x="1" y="1" width="20" height="14" fill="none" stroke="#fff" stroke-width="2"/><path d="M1 1l10 8 10-8" fill="none" stroke="#fff" stroke-width="2"/></svg>hello@velvetlune.style</div>
  </div>
  <div class="abs col col-products">
    <h4>PRODUCTS</h4>
    Gown<br>Skirt<br>Mini Skirt<br>Lorem<br>Ipsum
  </div>
  <div class="abs col col-social">
    <h4>SOCIAL LINKS</h4>
    <div class="row"><i></i>Circlefeed</div>
    <div class="row"><i></i>Chirpline</div>
    <div class="row"><i></i>Snapgrove</div>
    <div class="row"><i></i>Boardly</div>
    <div class="row"><i></i>Workweave</div>
  </div>
  <div class="abs footer-brand">
    <span class="brand-mark"></span>
    <span class="brand-name">VELVET LUNE</span>
  </div>
  <div class="abs copy">Copyright © 2018<br>All Rights Reserved.</div>
</footer>

</body>
</html>
```